Internal Office Slogans / Motto / Vision Statements

Hi. We would like to put up some posters around the office with quotations such as -
-”Do what you do so well that they will want to see it again and bring their friends.”- Hollis Trevane
-Make your customers feel heard and understood. Make your customers feel respected and liked. Make your customers feel appreciated and helped. Understand that you can do none of these things unless you are sincere about them.
Gregory Pilcott
- It’s a very predictable and satisfying phenomenon: whenever we get better, our customers do too.
Ray Casso
-Catch people in the act of performing extraordinary customer service. Treat them like heroes. Tell their stories, far and wide.
Tod Brinkerley

The purpose of the posters is to reiterate our culture and vision within the organisation. They should be clean, crisp and eye catching, not gaudy or bright. Professional, bold and strong.

The company website and logo is at http://www.nexolux.com.au
Print size will be A1

Thanks for participating & looking forward to seeing your great work.
Updates

Hi All. . 

So to reiterate we are looking for one background design to be used for multiple quotes...  The list of quotes are as follows: 

Support and or Sales Office

 

Make your customers feel heard and understood.Make your customers feel respected and liked. Make your customers feelappreciated and helped. Understand that you can do none of these things unlessyou are sincere about them.

Gregory Pilcott

 

Nothing liberates our greatness like the desireto help, the desire to serve

Rosalind Penhallow

 

It’s a very predictable and satisfying phenomenon:whenever we get better, our customers do too.

Ray Casso

 

Success means we go to sleep at night knowingthat our talents and abilities were used in a way that served others.

Rosalind Penhallow.

 

The sole purpose of business is to create, serveand satisfy a customer, from beginning to end – and that’s everyone’s job.

Tod Brinkerley

 

We don’t celebrate closing a sale, we celebrateopening a relationship.

Gwendolyn Asque

I will never make you a promise – unless I giveyou a plan and procedure to make that promise possible.

Bo Tarrick

 

Customers feel we take them for granted; onlyshow interest when we want an order; lavish our time on prospects; communicatemainly by invoice; are fixated on big accounts; drop them like hot potatoesonce we have the order; don’t follow through on promises; and satisfy our ownbureaucracy rather than their needs. We can do better than that, much better.

Peter L Osmund.

 

 

General and public area

 

Catch people in the act of performingextraordinary customer service. Treat them like heroes. Tell their stories, farand wide.

Tod Brinkerley

 

 

We see our customers as invited guests to aparty, and we are the hosts. It’s our job every day to make every importantaspect of the customer experience a little bit better." Carl Ingvold - Founder andCEO of Veltrix

 

"If you do build a great experience,customers tell each other about that. Word of mouth is verypowerful."  Carl Ingvold

 

It's not a faithin technology. It's faith in people. Neil Corrby

 

“Being the richest man in the cemetery doesn’tmatter to me … Going to bed at night saying we’ve done something wonderful…that’s what matters to me.” Neil Corrby

 

The customer experience is the next competitivebattleground. Lance Merriwether, CIO, Quorra Computers

 

”Do what you do so well that they will want tosee it again and bring their friends.”- Hollis Trevane

In the world of internet customer service, it isimportant to remember your competitor is only a mouse click away. GlenTrasky (not sure who he is but like the quote).

The customer is why you go to work. If they goaway, you do, too. Martin Glossop (?)

 

MaybeSome for Sales or Build Team:

Quality is remembered long after the price is forgotten. Varenne Family Slogan

```html
<!DOCTYPE html>
<html lang="en">
<head>
<meta charset="utf-8">
<title>Nexolux – Office Quote Poster</title>
<link rel="stylesheet" href="https://fonts.googleapis.com/css2?family=Anton&family=Archivo+Black&display=swap">
<style>
  :root {
    --ink: #000000;
    --signal-red: #cc0000;
    --deep-red: #7a0000;
    --paper-white: #ffffff;
    --author-grey: #e2e2e2;
  }
  * { margin: 0; padding: 0; box-sizing: border-box; }
  html, body {
    width: 848px;
    height: 1200px;
    overflow: hidden;
    background: var(--signal-red);
  }
  .poster {
    position: relative;
    width: 848px;
    height: 1200px;
    background: var(--signal-red);
    overflow: hidden;
  }
  .brand-band {
    position: absolute;
    top: 0; left: 0;
    width: 848px;
    height: 236px;
    background: var(--ink);
  }
  .brand-name {
    position: absolute;
    left: 36px;
    top: 10px;
    font-family: "Archivo Black", "Arial Black", sans-serif;
    font-size: 176px;
    line-height: 1;
    letter-spacing: -6px;
    color: var(--paper-white);
    white-space: nowrap;
  }
  .gauge-art {
    position: absolute;
    left: 670px;
    top: 890px;
    width: 178px;
    height: 310px;
    background: linear-gradient(160deg, var(--signal-red) 0%, var(--deep-red) 55%, var(--ink) 100%);
  }
  .quote {
    position: absolute;
    left: 34px;
    top: 256px;
    width: 780px;
    font-family: "Anton", "Impact", sans-serif;
    font-size: 100px;
    line-height: 118px;
    color: var(--ink);
    white-space: nowrap;
  }
  .quote-author {
    position: absolute;
    left: 64px;
    top: 990px;
    font-family: "Anton", "Impact", sans-serif;
    font-size: 92px;
    line-height: 1;
    color: var(--author-grey);
    white-space: nowrap;
  }
</style>
</head>
<body>
  <main class="poster">
    <header class="brand-band">
      <div class="brand-name">Nexolux</div>
    </header>

    <blockquote class="quote">“Do what you do<br>so well that they<br>will want to see<br>it again and<br>bring their<br>friends.”</blockquote>
    <p class="quote-author">- Hollis Trevane</p>

    <div class="gauge-art" role="img" aria-label="Dial gauge with a black needle in the lower right corner"></div>
  </main>
</body>
</html>
```